Insurance Agency website design for Vell Harbor Insurance, LP

Build a website for Vell Harbor Insurance, LP which sells Homeowners, Auto, Renters, Condo, Flood, Disability, Life, Umbrella, and health insurance. We need the coolest insurance agency website out there to get quotes, contact us, or get additional information. Please list the following insurance companies we work with: Dranko, Lisk, Corvane Mutual, Tremix, Wendmarch, QRZ, and Plumeworth.

Make a design similar to https://www.brimlockagents.example/

Selling personal insurance policies

```html
<!DOCTYPE html>
<html lang="en">
<head>
<meta charset="utf-8">
<title>Vell Harbor Insurance, LP</title>
<link href="https://fonts.googleapis.com/css2?family=Roboto:wght@400;500;700&family=Arimo:wght@400;700&display=swap" rel="stylesheet">
<style>
:root{
  --green:#12cc8f;
  --navy:#0b1f74;
  --navy-deep:#0d2a80;
  --ink:#1d1d1f;
  --paper:#ffffff;
  --mist:#f2f2f2;
  --field:#eeeeee;
}
*{margin:0;padding:0;box-sizing:border-box}
html,body{width:1200px;height:3678px;overflow:hidden}
body{position:relative;background:var(--paper);font-family:"Arimo",Arial,sans-serif;color:var(--ink)}
.abs{position:absolute}
h1,h2,h3,h4{font-family:"Roboto",Arial,sans-serif}

/* hero */
.hero{left:0;top:0;width:1200px;height:560px;background:linear-gradient(90deg,#d9cfc4 0%,#ece6de 40%,#f3f1ee 60%,#f5f4f2 100%)}
.nav{left:88px;top:20px;width:1024px;height:80px;border-radius:40px;background:var(--green)}
.nav ul{list-style:none;position:absolute;left:301px;top:0;height:80px;display:flex;align-items:center;gap:35px}
.nav a{color:#fff;text-decoration:none;font-family:"Roboto",sans-serif;font-weight:500;font-size:16px;position:relative}
.nav a.active::after{content:"";position:absolute;left:0;right:0;bottom:-9px;height:3px;background:#fff}
.nav .quote-btn{background:var(--navy);border-radius:22px;padding:11px 18px}
.brand{left:171px;top:-16px;width:160px;height:160px;border-radius:50%;background:#fff;display:flex;flex-direction:column;align-items:center;justify-content:center;padding-top:18px}
.brand .mark{width:34px;height:34px;border-radius:50%;background:var(--green);margin-bottom:8px}
.brand .name{font-family:"Roboto",sans-serif;font-weight:500;font-size:17px;color:var(--navy);line-height:1.1;text-align:center}
.hero-title{left:648px;top:160px;width:440px;font-size:42px;font-weight:700;line-height:48px;color:#222}
.hero-btn{left:648px;top:407px;width:125px;height:40px;border-radius:20px;background:var(--green);color:#fff;font-family:"Roboto";font-weight:700;font-size:16px;display:flex;align-items:center;justify-content:center}
.hero-next{left:1117px;top:312px}

/* welcome */
.welcome-kicker{left:147px;top:654px;font-size:19px;font-weight:700;font-family:"Roboto"}
.welcome-title{left:147px;top:682px;font-size:37px;font-weight:700;color:var(--navy)}
.welcome-title span{color:var(--green)}
.welcome-text{left:147px;top:732px;width:440px;font-size:15px;line-height:22.4px;text-align:justify}
.welcome-photo{left:636px;top:645px;width:421px;height:320px;background:linear-gradient(135deg,#b9c3cb,#8c8f93 50%,#3d4247)}
.welcome-corner{left:965px;top:628px;width:107px;height:108px;border-top:10px solid var(--navy);border-right:10px solid var(--navy)}
.contact-band{left:144px;top:885px;width:664px;height:168px;background:var(--green);color:#fff}
.contact-band .lead{position:absolute;left:32px;top:28px;font-family:"Roboto";font-weight:500;font-size:20px}
.contact-band .big{position:absolute;left:32px;top:50px;font-family:"Roboto";font-weight:500;font-size:38px}
.contact-item{position:absolute;left:330px;display:flex;gap:12px;align-items:center}
.contact-item .ico{width:44px;height:44px;border-radius:50%;background:#fff;display:flex;align-items:center;justify-content:center}
.contact-item b{display:block;font-size:16px}
.contact-item span{font-size:16px;font-weight:700}

/* partners */
.partners{left:0;top:1152px;width:1200px;height:569px;background:var(--mist)}
.partners h2{position:absolute;left:0;width:1200px;text-align:center;font-size:40px;font-weight:700;line-height:48px}
.partner{width:213px;height:130px;border:2px solid #c9c9c9;background:#fff;display:flex;align-items:center;justify-content:center;gap:10px;font-family:"Roboto";font-weight:700;font-size:22px;color:#222}
.partner i{width:16px;height:16px;background:#222;display:inline-block}

/* about */
.about{left:0;top:1721px;width:1200px;height:545px;background:linear-gradient(110deg,#1a3791 0%,#193488 55%,#203d99 100%)}
.about-dot{left:144px;top:1817px;width:110px;height:110px;border-radius:50%;background:var(--green)}
.about-ring{left:160px;top:1790px;width:392px;height:392px;border-radius:50%;background:var(--green)}
.about-photo{left:160px;top:1790px;width:384px;height:384px;border-radius:50%;background:linear-gradient(135deg,#f4f1ec,#d8d3cc 60%,#a89d92)}
.about-title{left:594px;top:1792px;font-size:40px;font-weight:700;color:#fff}
.about-text{left:594px;top:1852px;width:460px;color:#fff;font-size:15.5px;line-height:24px;text-align:justify}
.about-text p{margin-bottom:23px}

/* types */
.types-title{left:0;top:2328px;width:1200px;text-align:center;font-size:40px;font-weight:700;line-height:48px;color:#222}
.types-title span{color:var(--green)}
.type-card{top:2504px;width:220px;height:192px;border-radius:22px;background:var(--navy);color:#fff;display:flex;flex-direction:column;align-items:center;justify-content:center;gap:12px;font-family:"Roboto";font-weight:700;font-size:21px}

/* quote */
.quote{left:0;top:2786px;width:1200px;height:543px;background:var(--green)}
.quote-title{left:146px;top:2850px;font-size:40px;font-weight:700;color:#fff}
.quote-text{left:146px;top:2906px;width:409px;color:#fff;font-size:15.5px;line-height:24px;text-align:justify}
.quote-text p{margin-bottom:24px}
.quote-rule{left:624px;top:2894px;width:2px;height:350px;background:#fff}
.touch-title{left:678px;top:2863px;font-size:29px;font-weight:700;color:#fff}
.field{left:681px;width:376px;background:var(--field);font-size:15px;color:#333;padding:14px 15px}
.submit{left:682px;top:3206px;width:127px;height:42px;border-radius:21px;background:var(--navy);color:#fff;font-weight:700;font-size:16px;display:flex;align-items:center;justify-content:center}

/* footer */
.footer{left:0;top:3329px;width:1200px;height:349px;background:var(--navy)}
.foot-col h4{color:#fff;font-size:19px;font-weight:700;margin-bottom:16px}
.foot-col li{list-style:none;color:#fff;font-size:14px;line-height:25.5px;display:flex;gap:12px;align-items:center}
.foot-col li svg{flex:none}
.newsletter{left:811px;top:3439px;width:246px;height:40px;border-radius:20px;background:#fff;font-size:14px;padding:0 0 0 23px;display:flex;align-items:center;justify-content:space-between;padding-right:20px}
.foot-rule{left:143px;top:3607px;width:914px;height:1px;background:#4a5ea4}
.copyright{left:0;top:3629px;width:1200px;text-align:center;color:#fff;font-size:14px}
</style>
</head>
<body>

<section class="abs hero" role="img" aria-label="Photo of a couple and an insurance agent reviewing documents at a bright kitchen table"></section>
<nav class="abs nav">
  <ul>
    <li><a class="active">Home</a></li>
    <li><a>About</a></li>
    <li><a>Services</a></li>
    <li><a>Insurances</a></li>
    <li><a>Blog</a></li>
    <li><a>Contact</a></li>
    <li><a class="quote-btn">Get a Quote</a></li>
  </ul>
</nav>
<div class="abs brand"><span class="mark"></span><span class="name">Vell Harbor</span></div>
<h1 class="abs hero-title">At Vell Harbor Insurance,we understand that your peace of mind is invaluable.</h1>
<div class="abs hero-btn">Contact Us</div>
<svg class="abs hero-next" width="20" height="22" viewBox="0 0 20 22"><path d="M6 3l8 8-8 8" fill="none" stroke="#222" stroke-width="3"/></svg>

<h3 class="abs welcome-kicker">Welcome To</h3>
<h2 class="abs welcome-title">Vell Harbor <span>Insurance LP</span></h2>
<p class="abs welcome-text">At Vell Harbor Insurance, we understand that your peace of mind is invaluable. Our mission is to protect what matters most to you—your home, your vehicle, your health, and your loved ones. With our comprehensive range of insurance solutions, we are dedicated to safeguarding your assets and providing you with the security you deserve.</p>
<div class="abs welcome-corner"></div>
<div class="abs welcome-photo" role="img" aria-label="Photo of two clients meeting with an advisor in a glass-walled office"></div>
<div class="abs contact-band">
  <div class="lead">For inquiries, please</div>
  <div class="big">contact us at</div>
  <div class="contact-item" style="top:30px">
    <div class="ico"><svg width="18" height="18" viewBox="0 0 24 24"><path d="M6.6 10.8a15 15 0 006.6 6.6l2.2-2.2c.3-.3.7-.4 1-.2 1.1.4 2.3.6 3.6.6.6 0 1 .4 1 1V20c0 .6-.4 1-1 1A17 17 0 013 4c0-.6.4-1 1-1h3.5c.6 0 1 .4 1 1 0 1.3.2 2.5.6 3.6.1.3 0 .7-.2 1z" fill="#222"/></svg></div>
    <div><b>Phone:</b><span>(555) 014-2290</span></div>
  </div>
  <div class="contact-item" style="top:93px">
    <div class="ico"><svg width="18" height="14" viewBox="0 0 18 14"><rect width="18" height="14" rx="2" fill="#222"/><path d="M1 2l8 6 8-6" fill="none" stroke="#fff" stroke-width="1.5"/></svg></div>
    <div><b>Email:</b><span>info@vellharborinsurance.example</span></div>
  </div>
</div>

<section class="abs partners">
  <h2 style="top:76px;color:var(--navy)">Insurance Companies</h2>
  <h2 style="top:124px;color:var(--green)">We Work With</h2>
</section>
<div class="abs partner" style="left:143px;top:1344px">DRANKO</div>
<div class="abs partner" style="left:377px;top:1344px"><i></i>Lisk</div>
<div class="abs partner" style="left:611px;top:1344px;font-size:19px">Corvane Mutual</div>
<div class="abs partner" style="left:845px;top:1344px"><i></i>TREMIX</div>
<div class="abs partner" style="left:263px;top:1504px">Wendmarch</div>
<div class="abs partner" style="left:505px;top:1504px;font-size:34px">QRZ</div>
<div class="abs partner" style="left:746px;top:1504px">PLUMEWORTH</div>

<section class="abs about" role="img" aria-label="Deep blue band with faint foliage shading"></section>
<div class="abs about-dot"></div>
<div class="abs about-ring" style="left:168px"></div>
<div class="abs about-photo" role="img" aria-label="Photo of a hand signing a policy beside a small model house"></div>
<h2 class="abs about-title">About Us</h2>
<div class="abs about-text">
  <p>Vell Harbor Insurance is a full-service, independent insurance agency with over three decades of experience in delivering comprehensive insurance solutions to individuals.</p>
  <p>We proudly offer a diverse portfolio of products from more than 20 of the most reputable and financially secure companies in the industry. Our dedicated team of over 50 skilled professionals is committed to customizing these products and services to meet the unique needs of each client.</p>
  <p>At Vell Harbor Insurance, our experts are focused on addressing the individual needs of our clients, ensuring exceptional service and support at every step.</p>
</div>

<h2 class="abs types-title">Now More Specifically, What<br>They of Type <span>Personal Protection</span> Are You<br>Looking For?</h2>
<div class="abs type-card" style="left:147px">
  <svg width="100" height="62" viewBox="0 0 100 62"><circle cx="30" cy="31" r="30" fill="#fff"/><path d="M14 40v-10l10-2 8-10h24l10 10 10 2v10z" fill="var(--green)"/><circle cx="28" cy="42" r="6" fill="#fff" stroke="var(--green)" stroke-width="3"/><circle cx="66" cy="42" r="6" fill="#fff" stroke="var(--green)" stroke-width="3"/></svg>
  Auto</div>
<div class="abs type-card" style="left:377px">
  <svg width="90" height="62" viewBox="0 0 90 62"><circle cx="30" cy="31" r="30" fill="#fff"/><path d="M14 32L45 6l31 26h-9v26H23V32z" fill="var(--green)"/><rect x="38" y="40" width="14" height="18" fill="#fff"/></svg>
  Home</div>
<div class="abs type-card" style="left:606px">
  <svg width="90" height="62" viewBox="0 0 90 62"><circle cx="30" cy="31" r="30" fill="#fff"/><path d="M14 44c10-4 20-6 30-2l20-6c6-2 8 4 2 6L40 54H14z" fill="var(--green)"/><path d="M48 10c8 0 14 6 14 14l-14 6-14-6c0-8 6-14 14-14z" fill="var(--green)"/></svg>
  Renters</div>
<div class="abs type-card" style="left:836px">
  <svg width="90" height="62" viewBox="0 0 90 62"><circle cx="30" cy="31" r="30" fill="#fff"/><rect x="28" y="2" width="34" height="58" fill="var(--green)"/><rect x="18" y="24" width="14" height="36" fill="var(--green)"/><g fill="#fff"><rect x="34" y="8" width="6" height="6"/><rect x="48" y="8" width="6" height="6"/><rect x="34" y="22" width="6" height="6"/><rect x="48" y="22" width="6" height="6"/><rect x="34" y="36" width="6" height="6"/><rect x="48" y="36" width="6" height="6"/></g></svg>
  Condo</div>

<section class="abs quote"></section>
<h2 class="abs quote-title">Get a Quote</h2>
<div class="abs quote-text">
  <p>We believe that securing your home is one of the most important decisions you can make. Obtaining a comprehensive insurance quote is essential to understanding your coverage options and ensuring that your property is adequately protected against unforeseen events.</p>
  <p>Our team of experienced professionals is here to guide you through the process, helping you find the right policy that meets your specific needs and budget. Don't leave your home's safety to chance—get a quote today and take the first step towards peace of mind.</p>
</div>
<div class="abs quote-rule"></div>
<h2 class="abs touch-title">Get In Touch</h2>
<div class="abs field" style="top:2905px;height:47px">Enter Name</div>
<div class="abs field" style="top:2962px;height:47px">Enter Email</div>
<div class="abs field" style="top:3021px;height:47px">Enter Phone</div>
<div class="abs field" style="top:3079px;height:116px">Message</div>
<div class="abs submit">Submit</div>

<footer class="abs footer"></footer>
<div class="abs foot-col" style="left:143px;top:3396px">
  <h4>Our Company</h4>
  <ul><li>Our Story</li><li>News &amp; Blog</li><li>Careers</li><li>Customer Support</li><li>Contact Us</li><li>Website Accessibility</li></ul>
</div>
<div class="abs foot-col" style="left:350px;top:3396px">
  <h4>Our Offer</h4>
  <ul><li>Auto Insurance</li><li>Home Insurance</li><li>Claims</li><li>Agent Locator</li><li>Express Access</li><li>Money Back Policy</li></ul>
</div>
<div class="abs foot-col" style="left:539px;top:3396px">
  <h4>Contact info</h4>
  <ul>
    <li><svg width="12" height="12" viewBox="0 0 12 12"><path d="M6 0a4 4 0 014 4c0 3-4 8-4 8S2 7 2 4a4 4 0 014-4z" fill="var(--green)"/></svg>123,Lorem ipsum dolor sit</li>
    <li><svg width="12" height="12" viewBox="0 0 24 24"><path d="M6.6 10.8a15 15 0 006.6 6.6l2.2-2.2c.3-.3.7-.4 1-.2 1.1.4 2.3.6 3.6.6.6 0 1 .4 1 1V20c0 .6-.4 1-1 1A17 17 0 013 4c0-.6.4-1 1-1h3.5c.6 0 1 .4 1 1 0 1.3.2 2.5.6 3.6.1.3 0 .7-.2 1z" fill="var(--green)"/></svg>+1 888 888 8888</li>
    <li><svg width="12" height="10" viewBox="0 0 12 10"><rect width="12" height="10" rx="1" fill="var(--green)"/></svg>info@VellHarborInsurance.example</li>
    <li><svg width="12" height="12" viewBox="0 0 12 12"><circle cx="6" cy="6" r="6" fill="var(--green)"/><path d="M6 3v3h2" stroke="var(--navy)" fill="none"/></svg>Office Hours: 8AM - 11PM</li>
    <li style="padding-left:24px">Sunday - Wekend Day</li>
  </ul>
</div>
<div class="abs foot-col" style="left:813px;top:3396px"><h4>Newsletter</h4></div>
<div class="abs newsletter">Email address<svg width="16" height="16" viewBox="0 0 16 16"><path d="M0 7L16 0l-5 16-3-6z" fill="var(--green)"/></svg></div>
<div class="abs foot-rule"></div>
<div class="abs copyright">© Copyrights 2025 | All Rights Reserved</div>

</body>
</html>
```